Canadian company needs a packaging design for a new product line of TubNova Hot Tub & Bath Fragran

We are looking for a packaging design for a new company based in Edmonton, Alberta Canada called TubNova. We are developing a new product line of liquid and crystal Hot Tub & Bath Fragrances (aromatherapy) for example Lavender will be one of our fragrances. We are looking at the possibilities of using a stand up pouch and or the standard plastic bottles for our fragrance line. There will be different sizes from 150 grams to 600 grams in the crystal and 275 ml in the liquid. We would like to see bright multi-colored designs possibly with picture of the fragrance or a theme like favorite drinks or a more sensual idea. Each one of our fragrances will be a different color the main design needs to be able to have a different color of liquid or crystal in the bottle and possibly parts of the label will change colors for each fragrance. I have attached samples of another brand that we want to improve on.

Target Market(s)

Most of these fragrance are bought by women 70% men 30%
age 25 - 55

Industry/Entity Type

It Company

Requirements
Must have
• bottle size
Fragrance name
Nice to have
• Using the files below I like the circle of colors and possibly it could be made using water drops like in the file and possibly the two "S" could be designed like the third file I just added

```html
<!DOCTYPE html>
<html lang="en">
<head>
<meta charset="utf-8">
<title>TubNova Jasmine Label</title>
<link href="https://fonts.googleapis.com/css2?family=Open+Sans:wght@400;500;600;700&display=swap" rel="stylesheet">
<style>
  :root {
    --green-deep: #0f5a2e;
    --green-main: #1a8a5c;
    --green-soft: #5fb58e;
    --white: #ffffff;
    --ribbon: #e0203c;
    --ribbon-dark: #9c0f22;
    --tan: #8a6a2a;
  }
  html, body {
    margin: 0;
    padding: 0;
    width: 1200px;
    height: 709px;
    overflow: hidden;
    background: var(--white);
  }
  .label {
    position: relative;
    width: 1200px;
    height: 709px;
    font-family: "Open Sans", Arial, sans-serif;
  }
  .label-art {
    position: absolute;
    inset: 0;
    display: block;
  }
  .brand-name {
    font-weight: 600;
    font-size: 76px;
    fill: var(--green-deep);
  }
  .ribbon-text {
    font-weight: 600;
    fill: var(--white);
  }
  .fragrance-name {
    font-weight: 500;
    font-size: 34px;
    fill: var(--white);
  }
  .net-weight {
    font-weight: 500;
    font-size: 19px;
    fill: var(--tan);
  }
  .tagline {
    font-weight: 500;
    font-size: 20px;
    fill: var(--green-deep);
  }
</style>
</head>
<body>
<main class="label">
  <svg class="label-art" viewBox="0 0 1200 709" width="1200" height="709" xmlns="http://www.w3.org/2000/svg">
    <defs>
      <linearGradient id="bg-fill" x1="0" y1="0" x2="0" y2="1">
        <stop offset="0" stop-color="#1b8b5d"/>
        <stop offset="1" stop-color="#168556"/>
      </linearGradient>
      <radialGradient id="glow" cx="0.5" cy="0.5" r="0.5">
        <stop offset="0" stop-color="#ffffff" stop-opacity="0.35"/>
        <stop offset="0.6" stop-color="#ffffff" stop-opacity="0.1"/>
        <stop offset="1" stop-color="#ffffff" stop-opacity="0"/>
      </radialGradient>
      <linearGradient id="wave-fill" x1="0" y1="0" x2="0" y2="1">
        <stop offset="0" stop-color="#ffffff"/>
        <stop offset="0.55" stop-color="#f2f2f2"/>
        <stop offset="1" stop-color="#c9c9c9"/>
      </linearGradient>
      <radialGradient id="photo-fill" cx="0.62" cy="0.3" r="0.85">
        <stop offset="0" stop-color="#a8dcb8"/>
        <stop offset="0.3" stop-color="#cfd9c2"/>
        <stop offset="0.55" stop-color="#d2b27a"/>
        <stop offset="0.8" stop-color="#ecebe2"/>
        <stop offset="1" stop-color="#f7f6f0"/>
      </radialGradient>
      <linearGradient id="band-fill" x1="0" y1="0" x2="0" y2="1">
        <stop offset="0" stop-color="#ffffff"/>
        <stop offset="1" stop-color="#dcdcdc"/>
      </linearGradient>
      <clipPath id="above-band">
        <rect x="0" y="0" width="1200" height="663"/>
      </clipPath>
    </defs>

    <rect class="background" width="1200" height="709" fill="url(#bg-fill)"/>
    <ellipse class="background-glow" cx="600" cy="330" rx="520" ry="330" fill="url(#glow)"/>

    <rect class="top-strip" x="0" y="0" width="1200" height="30" fill="var(--green-deep)"/>
    <path class="wave-edge" d="M150,0 C300,30 410,252 600,254 C790,252 900,30 1050,0 Z" fill="var(--green-deep)"/>
    <path class="wave" d="M200,0 C330,30 430,232 600,234 C770,232 870,30 1000,0 Z" fill="url(#wave-fill)"/>

    <text class="brand-name" x="600" y="165" text-anchor="middle">TubNova</text>

    <g clip-path="url(#above-band)">
      <circle class="photo-ring" cx="600" cy="560" r="282" fill="var(--green-deep)"/>
      <circle class="photo" cx="600" cy="572" r="262" fill="url(#photo-fill)" role="img" aria-label="Rolled white towel beside a woven bowl of green bath crystals with white jasmine flowers"/>
      <circle class="fragrance-badge" cx="945" cy="620" r="90" fill="var(--green-deep)"/>
    </g>
    <text class="fragrance-name" x="945" y="626" text-anchor="middle">Jasmine</text>

    <g class="ribbon ribbon-top" transform="translate(215 552) rotate(-13)">
      <path d="M-135,-12 L-100,-12 L-100,30 L-135,30 L-122,9 Z" fill="var(--ribbon-dark)"/>
      <rect x="-112" y="-28" width="224" height="52" fill="var(--ribbon)"/>
      <text class="ribbon-text" x="0" y="10" text-anchor="middle" font-size="28">Spa &amp; Bath</text>
    </g>
    <g class="ribbon ribbon-bottom" transform="translate(280 604) rotate(-13)">
      <path d="M140,-18 L105,-18 L105,24 L140,24 L127,3 Z" fill="var(--ribbon-dark)"/>
      <rect x="-112" y="-22" width="224" height="42" fill="var(--ribbon)"/>
      <text class="ribbon-text" x="0" y="8" text-anchor="middle" font-size="23">Aromatherapy</text>
    </g>

    <path class="net-tab" d="M480,664 L480,646 Q480,632 494,632 L706,632 Q720,632 720,646 L720,664 Z" fill="var(--white)"/>
    <text class="net-weight" x="600" y="656" text-anchor="middle">100g Net</text>

    <rect class="bottom-band" x="0" y="663" width="1200" height="46" fill="url(#band-fill)"/>
    <text class="tagline" x="600" y="695" text-anchor="middle">A great aroma start to a well balanced body</text>
  </svg>
</main>
</body>
</html>
```